Social Media designs (LinkedIn banner, LinkedIn posts, Instagram)

Hello designers!
We are looking to create some more concepts for our social media identity for a search firm (recruitment company)
I have attached a "brand toolkit" that shows our brand, logo, colour scheme to guide you with regards to colours and identiy.

You will see in the brand toolkit there are some examples of;
- A LinkedIn banner for the company (page 23)
- Social Media posts for LinkedIn and Instagram (page 21)

What we are looking for...

We don't really like the current LinkedIn banner ideas. We would like to see more concepts that look more aesthetically pleasing - the current ideas look quite dull.

We DO like the social media post concepts but we would like to have more templates/options that we can use (similar themes)

We welcome submissions for Social Media designs that we can use with our company branding. Thank you for your work in advance!

```html
<!DOCTYPE html>
<html lang="en">
<head>
<meta charset="utf-8">
<title>Larkfield Search – LinkedIn Banner Concepts</title>
<link rel="stylesheet" href="https://fonts.googleapis.com/css2?family=EB+Garamond:wght@600&display=swap">
<style>
  :root {
    --board-grey: #707070;
    --forest: #132826;
    --stone: #e0dfd5;
    --paper: #ffffff;
  }
  html, body {
    margin: 0;
    padding: 0;
    width: 1200px;
    height: 1200px;
    overflow: hidden;
    background: var(--board-grey);
  }
  .presentation-board {
    display: block;
    width: 1200px;
    height: 1200px;
  }
  .banner-sheet { fill: var(--paper); filter: url(#sheet-shadow); }
  .emblem-field { fill: var(--paper); }
  .tagline, .brand-name {
    font-family: "EB Garamond", Garamond, Georgia, serif;
    font-weight: 600;
  }
  .tagline { font-size: 92px; letter-spacing: 1px; }
  .brand-name-large { font-size: 54px; letter-spacing: 2px; }
  .brand-name-small { font-size: 15px; letter-spacing: 1px; fill: var(--stone); }

  /* Dark-led variant */
  .variant-dark .tone-a { fill: var(--forest); }
  .variant-dark .tone-b { fill: var(--stone); }
  .variant-dark .tagline { fill: var(--stone); }
  .variant-dark .brand-name-large { fill: var(--stone); }

  /* Light-led variant */
  .variant-light .tone-a { fill: var(--stone); }
  .variant-light .tone-b { fill: var(--forest); }
  .variant-light .tagline { fill: var(--forest); }
  .variant-light .brand-name-large { fill: var(--forest); }
</style>
</head>
<body>
<svg class="presentation-board" viewBox="0 0 1932 1932" xmlns="http://www.w3.org/2000/svg">
  <defs>
    <filter id="sheet-shadow" x="-5%" y="-20%" width="110%" height="150%">
      <feDropShadow dx="0" dy="18" stdDeviation="12" flood-color="#000" flood-opacity="0.45"/>
    </filter>
    <clipPath id="banner-field">
      <rect x="117" y="507" width="1713" height="398"/>
    </clipPath>
  </defs>

  <!-- Banner concept 1: dark-led -->
  <g class="banner variant-dark">
    <rect class="banner-sheet" x="83" y="485" width="1767" height="442"/>
    <g clip-path="url(#banner-field)">
      <path class="tone-b" d="M117,507 L1830,507 L1830,905 L715,905 C450,810 230,680 117,507 Z"/>
      <path class="tone-a" d="M117,507 L140,507 C220,630 340,710 490,763 C380,690 290,600 250,507 L683,507 C1000,530 1250,580 1320,648 L1292,662 C1295,760 1310,830 1345,905 L715,905 C450,810 230,680 117,507 Z"/>
      <path class="tone-a" d="M1318,648 C1335,760 1400,860 1490,905 L1830,905 L1830,825 C1780,870 1700,900 1620,902 C1520,900 1450,870 1395,800 C1360,750 1340,700 1330,650 Z"/>
      <circle class="emblem-field" cx="1620" cy="632" r="270"/>
    </g>
    <text class="brand-name brand-name-small" x="103" y="633">LARKFIELD</text>
    <text class="tagline" x="1272" y="715" text-anchor="end">TALENT KNOWS</text>
    <text class="tagline" x="1272" y="812" text-anchor="end">NO BORDERS</text>
    <text class="brand-name brand-name-large" x="1632" y="668" text-anchor="middle">LARKFIELD</text>
    <text class="brand-name brand-name-large" x="1632" y="732" text-anchor="middle">SEARCH</text>
  </g>

  <!-- Banner concept 2: light-led -->
  <g class="banner variant-light" transform="translate(-1 570)">
    <rect class="banner-sheet" x="83" y="485" width="1767" height="442"/>
    <g clip-path="url(#banner-field)">
      <path class="tone-b" d="M117,507 L1830,507 L1830,905 L715,905 C450,810 230,680 117,507 Z"/>
      <path class="tone-a" d="M117,507 L140,507 C220,630 340,710 490,763 C380,690 290,600 250,507 L683,507 C1000,530 1250,580 1320,648 L1292,662 C1295,760 1310,830 1345,905 L715,905 C450,810 230,680 117,507 Z"/>
      <path class="tone-a" d="M1318,648 C1335,760 1400,860 1490,905 L1830,905 L1830,825 C1780,870 1700,900 1620,902 C1520,900 1450,870 1395,800 C1360,750 1340,700 1330,650 Z"/>
      <circle class="emblem-field" cx="1620" cy="632" r="270"/>
    </g>
    <text class="brand-name brand-name-small" x="103" y="633">LARKFIELD</text>
    <text class="tagline" x="1272" y="715" text-anchor="end">TALENT KNOWS</text>
    <text class="tagline" x="1272" y="812" text-anchor="end">NO BORDERS</text>
    <text class="brand-name brand-name-large" x="1632" y="668" text-anchor="middle">LARKFIELD</text>
    <text class="brand-name brand-name-large" x="1632" y="732" text-anchor="middle">SEARCH</text>
  </g>
</svg>
</body>
</html>
```